Design of professional looking Organizational Chart in Microsoft PowerPoint or Word

This is project is for an organizational chart to be designed in in either Microsoft Powerpoint or Word. I am requesting it in either of these so that I can make changes in the future. The final file will need to be delivered as a .pptx or .docx file.

I am attaching 2 items:
1-A PDF sketch of the organizational chart and how I want it to look. Please notice the detail of placement of each area. This is a sketch so you will need to make it as a appealing to the eye as possible, while keeping things where they need to be.

2-The Word document which includes the titles. This is if made available if you would like to copy/paste the titles in.

Please note that our logo and colors we prefer for the document and boxes are dark blue gray. We look forward to seeing high quality, professional looking submissions.

```html
<!DOCTYPE html>
<html lang="en">
<head>
<meta charset="utf-8">
<title>Church Organizational Chart</title>
<link href="https://fonts.googleapis.com/css2?family=Carlito&display=swap" rel="stylesheet">
<style>
  :root {
    --bg-center: #f4f2e9;
    --bg-mid: #e6e4dc;
    --bg-edge: #c4c4c4;
    --node: #3b3b3d;
    --node-text: #ffffff;
    --connector: #3a3f48;
    --connector-blue: #4a5a78;
  }
  html, body {
    margin: 0;
    padding: 0;
    width: 1200px;
    height: 856px;
    overflow: hidden;
  }
  .chart {
    position: relative;
    width: 1200px;
    height: 856px;
    background: radial-gradient(ellipse 62% 60% at 50% 46%, var(--bg-center) 0%, var(--bg-mid) 55%, var(--bg-edge) 100%);
    font-family: "Carlito", "Calibri", sans-serif;
  }
  .connectors {
    position: absolute;
    inset: 0;
    width: 1200px;
    height: 856px;
  }
  .node {
    position: absolute;
    box-sizing: border-box;
    display: flex;
    align-items: center;
    justify-content: center;
    padding: 0 14px;
    background: var(--node);
    color: var(--node-text);
    border-radius: 16px;
    font-size: 15px;
    line-height: 1.15;
    text-align: center;
    box-shadow: 0 4px 8px rgba(0, 0, 0, 0.35);
  }
  .node--left { justify-content: flex-start; text-align: left; }
  .node--tall-text { align-items: flex-start; padding-top: 4px; overflow: hidden; }

  .leadership { height: 46px; }
  .department { height: 43px; top: 345px; }
  .ministry { height: 43px; width: 168px; }
</style>
</head>
<body>
<main class="chart" aria-label="Church organizational chart">

  <svg class="connectors" viewBox="0 0 1200 856" aria-hidden="true">
    <defs>
      <marker id="arrow" viewBox="0 0 10 10" refX="9" refY="5" markerWidth="7" markerHeight="7" orient="auto-start-reverse">
        <path d="M0 1 L10 5 L0 9 z" fill="var(--connector)"/>
      </marker>
    </defs>
    <g fill="none" stroke="var(--connector)" stroke-width="1.4">
      <!-- board to leadership -->
      <line x1="607" y1="69" x2="607" y2="98" marker-end="url(#arrow)"/>
      <polyline points="397,140 397,111 817,111 817,140" marker-start="url(#arrow)" marker-end="url(#arrow)"/>
      <line x1="607" y1="132" x2="607" y2="284" marker-end="url(#arrow)"/>
      <!-- senior pastor to administrator -->
      <polyline points="315,168 171,168 171,199" marker-end="url(#arrow)"/>
      <!-- department drops -->
      <line x1="103" y1="396" x2="103" y2="418" marker-end="url(#arrow)"/>
      <line x1="313" y1="396" x2="313" y2="418" marker-end="url(#arrow)"/>
      <line x1="556" y1="396" x2="556" y2="418" marker-end="url(#arrow)"/>
      <line x1="947" y1="396" x2="947" y2="418" marker-end="url(#arrow)"/>
      <!-- ministry brackets -->
      <polyline points="73,455 37,455 37,817 73,817" marker-start="url(#arrow)" marker-end="url(#arrow)"/>
      <polyline points="297,455 272,455 272,604 297,604" marker-start="url(#arrow)" marker-end="url(#arrow)"/>
      <polyline points="533,455 507,455 507,672 533,672" marker-start="url(#arrow)" marker-end="url(#arrow)"/>
      <polyline points="895,455 864,455 864,528 895,528" marker-start="url(#arrow)" marker-end="url(#arrow)"/>
    </g>
    <g fill="none" stroke="var(--connector-blue)" stroke-width="1.4">
      <line x1="100" y1="312" x2="1100" y2="312"/>
      <line x1="100" y1="312" x2="100" y2="341" marker-end="url(#arrow)"/>
      <line x1="316" y1="312" x2="316" y2="341" marker-end="url(#arrow)"/>
      <line x1="505" y1="312" x2="505" y2="341" marker-end="url(#arrow)"/>
      <line x1="692" y1="312" x2="692" y2="341" marker-end="url(#arrow)"/>
      <line x1="908" y1="312" x2="908" y2="341" marker-end="url(#arrow)"/>
      <line x1="1100" y1="312" x2="1100" y2="341" marker-end="url(#arrow)"/>
    </g>
  </svg>

  <!-- leadership -->
  <div class="node leadership" style="left:485px; top:23px; width:243px;">Board of Directors</div>
  <div class="node leadership" style="left:315px; top:145px; width:178px;">Senior Pastor</div>
  <div class="node leadership" style="left:719px; top:144px; width:178px;">Elders</div>
  <div class="node leadership" style="left:75px; top:203px; width:193px;">Business Administrator</div>

  <!-- departments -->
  <div class="node department node--left" style="left:19px; width:166px;">Family ministry<br>pastor</div>
  <div class="node department node--left" style="left:229px; width:167px;">Outreach Pastor</div>
  <div class="node department node--left" style="left:421px; width:168px;">Helps Ministry<br>coordinator</div>
  <div class="node department" style="left:617px; width:168px;">Security</div>
  <div class="node department node--left" style="left:813px; width:168px;">Worship &amp; Media</div>
  <div class="node department node--left node--tall-text" style="left:1009px; width:168px; padding-top:7px;">Pastor’s<br>assistance</div>

  <!-- family ministries -->
  <div class="node ministry" style="left:75px; top:433px;">Children’s Ministry</div>
  <div class="node ministry" style="left:75px; top:505px;">Youth Ministry</div>
  <div class="node ministry" style="left:75px; top:583px;">College &amp; Career<br>Ministry</div>
  <div class="node ministry" style="left:75px; top:652px;">Men’s Ministry</div>
  <div class="node ministry" style="left:75px; top:725px;">Women’s Ministry</div>
  <div class="node ministry" style="left:75px; top:797px;">Men’s Ministry</div>

  <!-- outreach ministries -->
  <div class="node ministry" style="left:299px; top:433px;">Missions/Outreach</div>
  <div class="node ministry" style="left:299px; top:505px;">Care Ministry</div>
  <div class="node ministry" style="left:299px; top:583px;">Nursing Ministry</div>

  <!-- helps ministries -->
  <div class="node ministry" style="left:535px; top:433px;">Greeter Ministry</div>
  <div class="node ministry" style="left:535px; top:505px;">Ushers Ministry</div>
  <div class="node ministry" style="left:535px; top:583px;">Hospitality Ministry</div>
  <div class="node ministry" style="left:535px; top:652px;">Welcome Center</div>

  <!-- worship & media -->
  <div class="node ministry" style="left:897px; top:433px;">Worship Team</div>
  <div class="node ministry" style="left:897px; top:505px;">Media Ministry</div>

</main>
</body>
</html>
```